Luxury Skincare Product Box Packaging Design

Vorastelle is a range of skincare products that help protect, nourish, and strengthen even the most sensitive skin, ensuring it is healthy, glowing, calm, and soft. Skincare practices support skin to enhance its appearance and relieve skin conditions. Your skin reflects your health. It is your body canvas and is an asset. The products contain naturally derived ingredients, aromatherapy oils, sustainable and ethical ingredients, organic ingredients where possible, natural preservatives and Australian oils, fruits, and extracts.

Vorastelle
Tagline is "Where Calm Finds Bloom"

Our products do not contain sulphates, parabens, phthalates, petrochemicals, synthetic colours, nor synthetic fragrances.

Everything about the Vorastelle Skincare name is creative and communicates luxury. Vorastelle from your first glance of the name, you will know that this is a company with excellent products.

By keeping it simple, unique, and elegant is often associated with high quality and is a way to establish trust. Vorastelle is a product that is “pure” and natural, so Vorastelle packaging would look simple, elegant, and clean.

I have uploaded the actual logo design and individual labels for the current skincare range I currently with the ingredients included so you can get an understanding of what I like. I have also added samples of package designs I quite like to assist with your designs.

Each Product box packaging sizes are as follows:

Product One - Exfoliating Herbs: 110mm (H) x 33mm Diameter
Product Two - Probiotic Lotion: 138mm (H) x 33mm Diameter
Product Three - Vitamin A Serum: 120mm (H) x 30mm Diameter
Updates

The Measurements are as follows: Product One: 110mm (H) x 33mm Diameter Product Two: 138mm (H) x 33mm Diameter Product Three: 120mm (H) x 30mm Diameter

Target Market(s)

Women

Requirements
Must have
• Logo, Product Name and ingredients and if you can barcode on the packaging that is the box design I am after
Nice to have
• samples of designs I like but open to suggestions

```html
<!DOCTYPE html>
<html lang="en">
<head>
<meta charset="utf-8">
<title>Vorastelle Skincare – Box Dielines</title>
<link href="https://fonts.googleapis.com/css2?family=Open+Sans:wght@400;600;700&family=Roboto:wght@300;400&family=Open+Sans+Condensed:wght@700&display=swap" rel="stylesheet">
<style>
  :root{
    --backdrop:#e4d5c4;
    --board:#ffffff;
    --cut:#6f6f6f;
    --ink:#1c1c1c;
    --soft-ink:#555555;
    --rose-gold:#c08a72;
    --petal-light:#f3f3f3;
    --petal-mid:#dcdcdc;
  }
  *{margin:0;padding:0;box-sizing:border-box}
  html,body{width:960px;height:1200px;overflow:hidden;background:var(--backdrop)}
  .sheet{position:relative;width:960px;height:1200px;font-family:"Open Sans",sans-serif;color:var(--ink)}
  .dielines{position:absolute;left:0;top:0}
  .dielines polygon,.dielines rect,.dielines path{fill:var(--board);stroke:var(--cut);stroke-width:.6}
  .dielines line{stroke:var(--cut);stroke-width:.6}
  .abs{position:absolute}

  .ingredients{font-size:5.2px;line-height:8.6px;text-transform:uppercase;letter-spacing:-.05px}
  .ingredients b{font-size:6.6px;font-weight:700}
  .ingredients .organic{font-weight:700;display:block;padding-left:2px}
  .ingredients.large{font-size:8.1px;line-height:8.6px}
  .ingredients.large b,.ingredients.large .organic{font-family:"Open Sans Condensed",sans-serif;font-size:8.4px}

  .storage{border:.7px solid var(--ink);border-radius:4px;font-family:"Roboto",sans-serif;font-size:4.3px;line-height:5.9px;padding:2px 3px}

  .product-name{font-family:"Roboto",sans-serif;font-weight:300;text-align:center;font-size:10.4px;line-height:12.4px;color:#333}
  .skin-type{font-family:"Roboto",sans-serif;font-weight:300;text-align:center;font-size:5.8px;color:#555}
  .volume{font-family:"Roboto",sans-serif;font-weight:300;text-align:center;font-size:7px;color:#444}

  .claim{font-size:7.7px;line-height:7.6px}
  .directions{font-size:7.5px;line-height:10.3px}
  .directions strong{font-size:9.3px;font-weight:600}
  .directions .head{font-size:8.6px;font-weight:600;display:block;margin-bottom:1px}

  .floral{background:radial-gradient(ellipse at 45% 40%,var(--petal-light) 0%,var(--petal-mid) 55%,rgba(255,255,255,0) 75%)}

  .brand-name{position:absolute;font-family:"Roboto",sans-serif;font-weight:300;color:var(--rose-gold);white-space:nowrap;transform:translate(-50%,-50%) rotate(-90deg);letter-spacing:1px}
  .brand-name.front{font-size:22px}
  .brand-name.side{font-size:30px}

  .badges{position:absolute;display:flex;gap:0;align-items:flex-start}
  .badge{display:flex;flex-direction:column;align-items:center;font-family:"Roboto",sans-serif;font-size:2.4px;line-height:2.8px;text-align:center}
  .badge svg{display:block;margin-bottom:1px}
  .web{font-family:"Roboto",sans-serif;font-size:5px;text-align:center;transform:translateX(-50%)}
</style>
</head>
<body>
<div class="sheet">

<svg class="dielines" width="960" height="1200" viewBox="0 0 960 1200">
  <!-- Probiotic Face Lotion -->
  <g class="box-lotion">
    <polygon points="51.8,177 77.4,163.1 77.4,535.9 51.8,523.1"/>
    <path d="M166.4,163.1 V62.5 Q166.4,59.5 169.4,59.5 H252.4 Q255.4,59.5 255.4,62.5 V163.1 Z"/>
    <line x1="166.4" y1="73.5" x2="255.4" y2="73.5"/>
    <polygon points="87.9,96.3 163.6,96.3 163.6,163.1 77.4,163.1 87.9,157.5"/>
    <polygon points="258.2,96.3 333.9,96.3 333.9,151.5 344.5,163.1 258.2,163.1"/>
    <rect x="77.4" y="163.1" width="89" height="372.8"/>
    <rect x="166.4" y="163.1" width="89" height="372.8"/>
    <rect x="255.4" y="163.1" width="89.1" height="372.8"/>
    <rect x="344.5" y="163.1" width="89" height="372.8"/>
    <polygon points="77.4,535.9 163.6,535.9 163.6,602.1 87.9,602.1 87.9,545"/>
    <polygon points="258.2,535.9 344.5,535.9 333.9,547 333.9,602.1 258.2,602.1"/>
    <path d="M344.5,535.9 H433.5 V636.4 Q433.5,639.4 430.5,639.4 H347.5 Q344.5,639.4 344.5,636.4 Z"/>
    <line x1="344.5" y1="624.4" x2="433.5" y2="624.4"/>
  </g>
  <!-- Vitamin A Serum -->
  <g class="box-serum">
    <polygon points="535.4,232.6 563.2,215.9 563.2,539.8 535.4,520.3"/>
    <path d="M644.4,215.9 V119.9 Q644.4,116.9 647.4,116.9 H722.7 Q725.7,116.9 725.7,119.9 V215.9 Z"/>
    <line x1="644.4" y1="134.7" x2="725.7" y2="134.7"/>
    <polygon points="573.2,156.4 642.2,156.4 642.2,215.9 563.2,215.9 573.2,210"/>
    <polygon points="727.9,156.4 796.9,156.4 796.9,206 806.4,215.9 727.9,215.9"/>
    <rect x="563.2" y="215.9" width="81.2" height="323.9"/>
    <rect x="644.4" y="215.9" width="81.3" height="323.9"/>
    <rect x="725.7" y="215.9" width="80.7" height="323.9"/>
    <rect x="806.4" y="215.9" width="81.2" height="323.9"/>
    <polygon points="563.2,539.8 642.2,539.8 642.2,599.9 573.2,599.9 573.2,548"/>
    <polygon points="727.9,539.8 806.4,539.8 796.9,549.5 796.9,599.9 727.9,599.9"/>
    <path d="M806.4,539.8 H887.6 V635.9 Q887.6,638.9 884.6,638.9 H809.4 Q806.4,638.9 806.4,635.9 Z"/>
    <line x1="806.4" y1="621.1" x2="887.6" y2="621.1"/>
  </g>
  <!-- Gentle Exfoliating Herbs -->
  <g class="box-herbs">
    <polygon points="346.1,779.1 370.1,770.2 370.1,1067.4 346.1,1054.6"/>
    <path d="M459.1,770.2 V669.7 Q459.1,666.7 462.1,666.7 H545.2 Q548.2,666.7 548.2,669.7 V770.2 Z"/>
    <line x1="459.1" y1="681.2" x2="548.2" y2="681.2"/>
    <polygon points="380.6,704 455.8,704 455.8,770.2 370.1,770.2 380.6,764"/>
    <polygon points="550.9,704 626.6,704 626.6,759 637.2,770.2 550.9,770.2"/>
    <rect x="370.1" y="770.2" width="89" height="297.2"/>
    <rect x="459.1" y="770.2" width="89.1" height="297.2"/>
    <rect x="548.2" y="770.2" width="89" height="297.2"/>
    <rect x="637.2" y="770.2" width="89" height="297.2"/>
    <polygon points="370.1,1067.4 455.8,1067.4 455.8,1133.6 380.6,1133.6 380.6,1077"/>
    <polygon points="550.9,1067.4 637.2,1067.4 626.6,1078 626.6,1133.6 550.9,1133.6"/>
    <path d="M637.2,1067.4 H726.2 V1167.9 Q726.2,1170.9 723.2,1170.9 H640.2 Q637.2,1170.9 637.2,1167.9 Z"/>
    <line x1="637.2" y1="1156.4" x2="726.2" y2="1156.4"/>
  </g>
</svg>

<!-- ============ Probiotic Face Lotion ============ -->
<section class="box lotion">
  <p class="abs ingredients" style="left:81.8px;top:235px;width:84px">
    <b>Ingredients:</b> Aloe barbadensis (aloe vera) leaf juice, rosa eglanteria (rosehip) oil*, coco-glucoside, agave americana leaf extract, lactobacillus bulgaricus ferment filtrate, eucalyptus globulus (tasmanian blue gum extract) stearic acid (vegetable derived), glyceryl stearate (vegetable derived), glycerin*, cucumis sativus (cucumber) seed oil, salix alba (white willow bark), xanthus gum, cetearyl alcohol (coconut derived), teriminalia origanum vulgare oil, thymus vulgaris extract, olea europeia leaf extract, rosmarinus officinalis leaf extract, lavandula angustifolia (lavender) flower extract, pelargonium graveolens (geranium) oil
    <span class="organic">*Organic ingredients</span>
  </p>
  <p class="abs storage" style="left:81.3px;top:490.3px;width:78px;height:34.5px">Store in a cool dry place Caution For external use only. Avoid contact with eyes. If irritation occurs, discontinue use.</p>

  <div class="abs floral" role="img" aria-label="Fine grey line drawing of wild blossoms and leaves" style="left:168.6px;top:214px;width:79px;height:136px"></div>
  <span class="brand-name front" style="left:208.7px;top:300.5px">Vorastelle</span>
  <p class="abs product-name" style="left:166.4px;top:452px;width:89px">Probiotic Face<br>Lotion</p>
  <p class="abs skin-type" style="left:166.4px;top:479px;width:89px">All Skin Types</p>
  <p class="abs volume" style="left:166.4px;top:506px;width:89px">60ml</p>

  <p class="abs claim" style="left:263.8px;top:240.4px;width:80px">All Skin Types - Innovative moisturising lotion soothes and settles problematic and blemish prone complexions.</p>
  <p class="abs directions" style="left:262.1px;top:313px;width:78px"><strong>Directions:</strong> Apply a small amount to your face morning and night after cleansing. Avoid eye area.</p>
  <div class="badges" style="left:256px;top:472px">
    <div class="badge" style="width:16px"><svg width="10" height="10" viewBox="0 0 10 10"><circle cx="5" cy="5" r="4" fill="none" stroke="#222" stroke-width=".7"/></svg>Australian<br>Made</div>
    <div class="badge" style="width:16px"><svg width="10" height="10" viewBox="0 0 10 10"><path d="M5 8.6 1.3 5A2.1 2.1 0 0 1 5 2.6 2.1 2.1 0 0 1 8.7 5Z" fill="none" stroke="#222" stroke-width=".7"/></svg>100%<br>Vegan</div>
    <div class="badge" style="width:16px"><svg width="10" height="10" viewBox="0 0 10 10"><rect x="1.5" y="1.5" width="7" height="7" rx="1" fill="none" stroke="#222" stroke-width=".7"/></svg>Cruelty<br>Free</div>
    <div class="badge" style="width:22px"><svg width="11" height="10" viewBox="0 0 11 10"><path d="M5.5 1 8 5H3ZM2 6.5 4.5 9H1ZM9 6.5 10 9H6.5Z" fill="#222"/></svg>Please<br>Recycle</div>
    <div class="badge" style="width:20px"><svg width="10" height="10" viewBox="0 0 10 10"><rect x="2" y="1.5" width="6" height="2" fill="none" stroke="#222" stroke-width=".7"/><rect x="1.5" y="4" width="7" height="4.5" rx="1" fill="none" stroke="#222" stroke-width=".7"/></svg>6 months<br>once open</div>
  </div>
  <p class="abs web" style="left:300px;top:504px">www.vorastelle.com</p>

  <span class="brand-name side" style="left:389.6px;top:356px">Vorastelle</span>
</section>

<!-- ============ Vitamin A Serum ============ -->
<section class="box serum">
  <p class="abs ingredients" style="left:568.7px;top:277px;width:76px">
    <b>Ingredients: :</b><br>Simmondsia chinensis (jojoba) seed oil*, persea gratissima (avocado) oil, rosa eglanteria (rosehip) oil*, olea europaea (olive) fruit oil*, hippophae rhamnoides (seabuckthorn berry) kernal extract*, tocopherol (vitamin e), retinyl palmitate (vitamin a), glycine soja oilboswellia carterii oil (frankincense), pelargonium roseum leaf oil, (rose geranium), cananga odorata flower oil (ylang ylang), rosmarinus officianlis leaf extract
    <span class="organic">*Organic ingredients</span>
  </p>
  <p class="abs storage" style="left:565.4px;top:482.5px;width:76.8px;height:34px">Store in a cool dry place Caution For external use only. Avoid contact with eyes. If irritation occurs, discontinue use.</p>

  <div class="abs floral" role="img" aria-label="Fine grey line drawing of open wild roses" style="left:648px;top:289px;width:75px;height:156px"></div>
  <span class="brand-name front" style="left:684.5px;top:345px">Vorastelle</span>
  <p class="abs product-name" style="left:644.4px;top:468px;width:81.3px">Vitamin A<br>Serum</p>
  <p class="abs skin-type" style="left:644.4px;top:494px;width:81.3px">All Skin Types</p>
  <p class="abs volume" style="left:644.4px;top:520px;width:81.3px">30ml</p>

  <p class="abs claim" style="left:732.4px;top:273.8px;width:74px">All Skin Types - Particularly beneficial for dry, Mature skins</p>
  <p class="abs directions" style="left:731.8px;top:321px;width:74px"><span class="head">Directions:</span>Directions: Massage &nbsp;a small amount into your face at night, avoiding eye area. Follow with your favourite moisturiser. Please note: Do not use on pregnant or breast-feeding women.</p>
  <div class="badges" style="left:729px;top:466px">
    <div class="badge" style="width:13px"><svg width="8" height="8" viewBox="0 0 10 10"><circle cx="5" cy="5" r="4" fill="none" stroke="#222" stroke-width=".7"/></svg>Australian<br>Made</div>
    <div class="badge" style="width:13px"><svg width="8" height="8" viewBox="0 0 10 10"><path d="M5 8.6 1.3 5A2.1 2.1 0 0 1 5 2.6 2.1 2.1 0 0 1 8.7 5Z" fill="none" stroke="#222" stroke-width=".7"/></svg>100%<br>Vegan</div>
    <div class="badge" style="width:14px"><svg width="8" height="8" viewBox="0 0 10 10"><rect x="1.5" y="1.5" width="7" height="7" rx="1" fill="none" stroke="#222" stroke-width=".7"/></svg>Cruelty<br>Free</div>
    <div class="badge" style="width:17px"><svg width="9" height="8" viewBox="0 0 11 10"><path d="M5.5 1 8 5H3ZM2 6.5 4.5 9H1ZM9 6.5 10 9H6.5Z" fill="#222"/></svg>Please<br>Recycle</div>
    <div class="badge" style="width:18px"><svg width="8" height="8" viewBox="0 0 10 10"><rect x="2" y="1.5" width="6" height="2" fill="none" stroke="#222" stroke-width=".7"/><rect x="1.5" y="4" width="7" height="4.5" rx="1" fill="none" stroke="#222" stroke-width=".7"/></svg>6 months<br>once open</div>
  </div>
  <p class="abs web" style="left:764.6px;top:506px">www.vorastelle.com</p>

  <span class="brand-name side" style="left:845.9px;top:384px">Vorastelle</span>
</section>

<!-- ============ Gentle Exfoliating Herbs ============ -->
<section class="box herbs">
  <p class="abs ingredients large" style="left:373.4px;top:830px;width:84px">
    <b>Ingredients:</b> Oryza sativa (rice) powder*, rosa gallica (rose petals)*, jasminum officinale (jasmine) flower, matricaria re cutita (chamomile flowers)*, camellia sinensis leaf (green tea), luffa cylindrica fruit powder, calendula officinalis (marigold flowers)
    <span class="organic">*Organic ingredients</span>
  </p>
  <p class="abs storage" style="left:375.6px;top:991.7px;width:78px;height:35px">Store in a cool dry place Caution For external use only. Avoid contact with eyes. If irritation occurs, discontinue use.</p>

  <div class="abs floral" role="img" aria-label="Soft grey drawing of a blooming rose with leaves" style="left:464.7px;top:818px;width:80.7px;height:156px"></div>
  <span class="brand-name front" style="left:503.6px;top:890.4px">Vorastelle</span>
  <p class="abs product-name" style="left:459.1px;top:994.5px;width:89.1px">Gentle<br>Exfoliating Herbs</p>
  <p class="abs skin-type" style="left:459.1px;top:1020.5px;width:89.1px">All Skin Types</p>
  <p class="abs volume" style="left:459.1px;top:1038px;width:89.1px">40ml</p>

  <p class="abs claim" style="left:551.5px;top:831.4px;width:84px">All Skin Types - Particularly beneficial for Sensitive, stressed and delicate skin.</p>
  <p class="abs directions" style="left:552.6px;top:895px;width:82px"><strong>Directions:</strong> Mix a small amount with your favourite cleanser. Massage into your face for approxi-mately one minute before removing with water or a face cloth. Use twice weekly.</p>
  <div class="badges" style="left:549px;top:1002px">
    <div class="badge" style="width:16px"><svg width="10" height="10" viewBox="0 0 10 10"><circle cx="5" cy="5" r="4" fill="none" stroke="#222" stroke-width=".7"/></svg>Australian<br>Made</div>
    <div class="badge" style="width:16px"><svg width="10" height="10" viewBox="0 0 10 10"><path d="M5 8.6 1.3 5A2.1 2.1 0 0 1 5 2.6 2.1 2.1 0 0 1 8.7 5Z" fill="none" stroke="#222" stroke-width=".7"/></svg>100%<br>Vegan</div>
    <div class="badge" style="width:16px"><svg width="10" height="10" viewBox="0 0 10 10"><rect x="1.5" y="1.5" width="7" height="7" rx="1" fill="none" stroke="#222" stroke-width=".7"/></svg>Cruelty<br>Free</div>
    <div class="badge" style="width:22px"><svg width="11" height="10" viewBox="0 0 11 10"><path d="M5.5 1 8 5H3ZM2 6.5 4.5 9H1ZM9 6.5 10 9H6.5Z" fill="#222"/></svg>Please<br>Recycle</div>
    <div class="badge" style="width:20px"><svg width="10" height="10" viewBox="0 0 10 10"><rect x="2" y="1.5" width="6" height="2" fill="none" stroke="#222" stroke-width=".7"/><rect x="1.5" y="4" width="7" height="4.5" rx="1" fill="none" stroke="#222" stroke-width=".7"/></svg>6 months<br>once open</div>
  </div>
  <p class="abs web" style="left:592.7px;top:1034px">www.vorastelle.com</p>

  <span class="brand-name side" style="left:683.4px;top:918.2px">Vorastelle</span>
</section>

</div>
</body>
</html>
```